Bluestone Advisory & Mgmt - Professional Business Cards

Hi!

I am a Real Estate Developer and Construction Consultant.

I have a lot of inspiration from previous designs and would be open to using the attached Designs as a starting point. I would like to see these styles incorporated into your designs.

I really need professional business card to go with it that includes my important info.

Look forward to seeing your designs!.

Target Market(s)

My Target market are building owners, lawyers, consultants.

Industry/Entity Type

Real Estate Development

Contact Information for Business Card

My Name: Dorian Pelkey
My Title: Principle
Company Name: Bluestone Advisory & Mgmt, LLC
Address: 348 West 71st Street, 9th FL New York, NY 10010
Mobile: 917.806.3971
Website: bam-hvx.example

Font styles to use
Serif
Sans Serif

Colors

Designer to choose colors to be used in the design.

Requirements
Must have
• Must incorporate the logo attached or have new that looks similar.
• Must use professional font that will be seen and judged by wealthy land owners and developers.
• Must incorporate some of the color green.
Should not have
• Photo's or pictures of people or buildings of any kind.

```html
<!DOCTYPE html>
<html lang="en">
<head>
<meta charset="utf-8">
<title>Bluestone Advisory &amp; Mgmt – Business Cards</title>
<link rel="stylesheet" href="https://fonts.googleapis.com/css2?family=Open+Sans:wght@400;600&family=Oswald:wght@300&family=PT+Sans+Narrow:wght@400&display=swap">
<style>
  :root {
    --backdrop: #000000;
    --charcoal: #433c3d;
    --paper: #ffffff;
    --ink: #1c1a1a;
    --text-muted: #3f3a3b;
    --rule: #8a8485;
    --accent-green: #4dbb7b;
  }
  * { margin: 0; padding: 0; box-sizing: border-box; }
  html, body {
    width: 1009px;
    height: 1200px;
    overflow: hidden;
    background: var(--backdrop);
  }
  .canvas {
    position: relative;
    width: 1009px;
    height: 1200px;
  }
  .card-front {
    position: absolute;
    left: 28px; top: 28px;
    width: 954px; height: 544px;
    background: var(--charcoal);
  }
  .front-wordmark {
    position: absolute;
    left: 0; right: 0; top: 0; bottom: 0;
    display: flex;
    align-items: center;
    justify-content: center;
    padding-left: 110px;
    color: var(--paper);
    font-family: "Oswald", sans-serif;
    font-weight: 300;
    font-size: 92px;
    letter-spacing: 2px;
    text-transform: uppercase;
  }
  .card-back {
    position: absolute;
    left: 28px; top: 628px;
    width: 954px; height: 545px;
    background: var(--paper);
  }
  .card-frame {
    position: absolute;
    left: 27px; top: 27px;
    width: 900px; height: 491px;
    border: 2px solid var(--charcoal);
  }
  .contact {
    position: absolute;
    right: 572px;
    top: 0;
    text-align: right;
    white-space: nowrap;
  }
  .contact-name {
    position: absolute; right: 0; top: 222px;
    font-family: "Open Sans", sans-serif;
    font-size: 26px;
    color: var(--ink);
    line-height: 1;
  }
  .contact-title {
    position: absolute; right: 0; top: 266px;
    font-family: "Open Sans", sans-serif;
    font-size: 24px;
    color: var(--ink);
    line-height: 1;
  }
  .contact-rule {
    position: absolute; right: 0;
    width: 145px;
    border-top: 2px solid var(--rule);
  }
  .rule-one { top: 254px; }
  .rule-two { top: 300px; }
  .contact-details {
    position: absolute; right: 0; top: 314px;
    font-family: "PT Sans Narrow", sans-serif;
    font-size: 21px;
    line-height: 31px;
    color: var(--text-muted);
    font-style: normal;
  }
  .contact-details .gap { margin-top: 6px; line-height: 25px; }
  .company-mark {
    position: absolute;
    left: 412px;
    top: 220px;
  }
  .company-square {
    position: absolute;
    left: 0; top: 0;
    width: 28px; height: 84px;
    border-radius: 14px;
    background: var(--accent-green);
  }
  .company-name {
    position: absolute;
    left: 46px; top: -6px;
    font-family: "Open Sans", sans-serif;
    font-weight: 600;
    font-size: 51px;
    line-height: 48px;
    color: var(--charcoal);
    text-transform: uppercase;
    white-space: nowrap;
  }
</style>
</head>
<body>
<main class="canvas">
  <section class="card-front">
    <div class="front-wordmark">Bluestone</div>
  </section>

  <section class="card-back">
    <div class="card-frame"></div>

    <div class="contact">
      <div class="contact-name">DORIAN PELKEY</div>
      <div class="contact-rule rule-one"></div>
      <div class="contact-title">PRINCIPAL</div>
      <div class="contact-rule rule-two"></div>
      <address class="contact-details">
        <div>348 WEST 71ST STREET, 9TH FL</div>
        <div>NEW YORK, NY 10010</div>
        <div class="gap">917.806.3971</div>
        <div style="line-height:25px">bam-hvx.example</div>
        <div style="line-height:25px">dorian@bam-hvx.example</div>
      </address>
    </div>

    <div class="company-mark">
      <div class="company-square"></div>
      <div class="company-name">Bluestone<br>Advisory &amp;<br>Mgmt, LLC</div>
    </div>
  </section>
</main>
</body>
</html>
```